TRV business card

Need a business card for a company that provides instructional design and elearning development services. The website is here: http://tarvexa.studio/

I'm attaching a current logo, as well as the old business card design. While I like to keep it clean, the old design is too simplistic for my liking. The only idea I want to reuse from the old design is placing industry jargon on the back of the card, just need a better way to present it. But if you have other ideas for the back--feel free to experiment.

Please use the colors complementary to the color we have on the website. Thank you!

```html
<!DOCTYPE html>
<html lang="en">
<head>
<meta charset="utf-8">
<title>TRV business card</title>
<link rel="stylesheet" href="https://fonts.googleapis.com/css2?family=Montserrat:wght@400;600;700&family=Oswald:wght@400;500&display=swap">
<style>
  :root {
    --teal: #1db3ab;
    --teal-dark: #12a29a;
    --gold: #c8b67f;
    --ink: #3b3b3b;
    --ink-soft: #555555;
    --paper: #ffffff;
    --backdrop: #e7e7e5;
    --line: #444444;
  }
  * { margin: 0; padding: 0; box-sizing: border-box; }
  html, body { width: 1200px; height: 1120px; overflow: hidden; }
  body { background: var(--backdrop); position: relative; font-family: "Montserrat", sans-serif; }

  .card {
    position: absolute; left: 170px; width: 860px; height: 491px;
    background: var(--paper); overflow: hidden;
    box-shadow: 0 6px 18px rgba(0,0,0,.18);
  }
  .card--front { top: 36px; }
  .card--back { top: 593px; }

  /* front */
  .brand {
    position: absolute; top: 46px; right: 70px;
    display: flex; align-items: center; gap: 16px;
  }
  .brand__dot { width: 34px; height: 34px; background: var(--teal); }
  .brand__name { font-weight: 700; font-size: 44px; color: var(--gold); letter-spacing: .5px; }

  .name-tag { position: absolute; left: 0; top: 170px; width: 330px; height: 84px; }
  .name-tag svg { position: absolute; inset: 0; }
  .name-tag__text { position: absolute; left: 34px; top: 12px; color: var(--paper); }
  .name-tag__name { font-weight: 700; font-size: 22px; line-height: 30px; }
  .name-tag__role { font-weight: 400; font-size: 20px; line-height: 28px; }

  .contacts { position: absolute; left: 44px; top: 300px; list-style: none; }
  .contacts li { display: flex; align-items: center; gap: 12px; font-size: 16px; color: var(--ink-soft); height: 36px; }
  .contacts svg { width: 18px; height: 18px; }

  .front-band { position: absolute; left: 0; bottom: 0; width: 860px; height: 110px; }

  /* back */
  .headline {
    position: absolute; left: 48px; top: 40px;
    font-family: "Oswald", sans-serif; font-weight: 400;
    font-size: 100px; line-height: 102px; color: var(--ink); letter-spacing: 1px;
  }
  .services { position: absolute; left: 290px; top: 30px; width: 540px; height: 440px; }
  .services svg { position: absolute; left: 0; top: 0; }
  .services ul { list-style: none; position: absolute; left: 110px; top: 0; }
  .services li {
    font-family: "Oswald", sans-serif; font-weight: 500; font-size: 31px;
    line-height: 72px; height: 72px; color: var(--ink); letter-spacing: .6px; white-space: nowrap;
  }
</style>
</head>
<body>

<section class="card card--front">
  <div class="brand">
    <span class="brand__dot"></span>
    <span class="brand__name">Tarvexa Studio</span>
  </div>

  <div class="name-tag">
    <svg width="330" height="84" viewBox="0 0 330 84"><polygon points="0,0 290,0 330,84 0,84" fill="var(--teal)"/></svg>
    <div class="name-tag__text">
      <div class="name-tag__name">Daniel Forsberg</div>
      <div class="name-tag__role">Managing Director</div>
    </div>
  </div>

  <ul class="contacts">
    <li><svg viewBox="0 0 20 20"><circle cx="10" cy="10" r="9" fill="var(--teal)"/><path d="M7 5l2 3-1 1c1 2 2 3 3 3l1-1 3 2-1 2c-4 0-8-4-8-8z" fill="#fff"/></svg>555-014-2290</li>
    <li><svg viewBox="0 0 20 20"><circle cx="10" cy="10" r="8" fill="none" stroke="var(--teal)" stroke-width="2"/><ellipse cx="10" cy="10" rx="3.5" ry="8" fill="none" stroke="var(--teal)" stroke-width="1.5"/><line x1="2" y1="10" x2="18" y2="10" stroke="var(--teal)" stroke-width="1.5"/></svg>www.tarvexa.studio</li>
    <li><svg viewBox="0 0 20 20"><circle cx="10" cy="10" r="9" fill="var(--teal)"/><rect x="5" y="6.5" width="10" height="7" fill="#fff"/><path d="M5 6.5l5 4 5-4" fill="none" stroke="var(--teal)" stroke-width="1.2"/></svg>dforsberg@tarvexa.studio</li>
  </ul>

  <svg class="front-band" viewBox="0 0 860 110" preserveAspectRatio="none">
    <polygon points="0,92 500,72 520,40 860,22 860,110 0,110" fill="var(--teal)"/>
    <polygon points="0,110 0,98 500,78 520,46 860,28 860,36 530,52 510,84 0,110" fill="var(--teal-dark)" opacity=".5"/>
  </svg>
</section>

<section class="card card--back">
  <h1 class="headline">HOW<br>CAN<br>WE<br>HELP?</h1>

  <div class="services">
    <svg width="110" height="440" viewBox="0 0 110 440" fill="none" stroke="var(--line)" stroke-width="1.6">
      <line x1="50" y1="36" x2="50" y2="396"/>
      <g fill="#fff">
        <polygon points="50,20 92,36 50,52 8,36"/>
        <polygon points="50,92 92,108 50,124 8,108"/>
        <polygon points="50,164 92,180 50,196 8,180"/>
        <polygon points="50,236 92,252 50,268 8,252"/>
        <polygon points="50,308 92,324 50,340 8,324"/>
        <polygon points="50,380 92,396 50,412 8,396"/>
      </g>
      <rect x="45" y="28" width="10" height="16" rx="1.5"/>
      <rect x="42" y="102" width="16" height="11"/><line x1="46" y1="106" x2="54" y2="106"/>
      <path d="M44 173h12l-1.5 13-4.5 2-4.5-2z"/>
      <circle cx="50" cy="250" r="4"/><line x1="48" y1="256" x2="52" y2="256"/>
      <circle cx="50" cy="322" r="6"/><circle cx="50" cy="322" r="2" fill="var(--line)"/>
      <rect x="44" y="389" width="14" height="10"/><line x1="48" y1="403" x2="54" y2="403"/>
    </svg>
    <ul>
      <li>MOBILE LEARNING SCORM</li>
      <li>INSTRUCTIONAL DESIGN LMS</li>
      <li>MOOCS ELEARNING HTML5</li>
      <li>ADULT LEARNING THEORY</li>
      <li>GAMIFICATION CLASSROOM</li>
      <li>XAPI BLENDED LEARNING</li>
    </ul>
  </div>
</section>

</body>
</html>
```